We are a music company that specializes in Music Mixing and Mastering. We also do vocal recording and create instrumentals for various artists. Our website is 738kv.com

Target Market(s)

Musicians, Record labels, rappers, and singers

Industry/Entity Type

Artists

Contact Information for Business Card

738KV
Industry Standard Mixing & Mastering
(555) 214-3907
sales@738kv.com
738kv.com

Requirements
Must have
• contact info and twitter (@738KV)

```html
<!DOCTYPE html>
<html lang="en">
<head>
<meta charset="utf-8">
<title>738KV Business Card</title>
<link rel="stylesheet" href="https://fonts.googleapis.com/css2?family=Pathway+Gothic+One&display=swap">
<style>
  :root {
    --page-bg: #e9e9e9;
    --card-light: #ffffff;
    --card-dark: #2b2a2b;
    --ink: #1c1c1c;
    --text-light: #f2f2f2;
    --art-grey: #d4d4d4;
  }
  * { margin: 0; padding: 0; box-sizing: border-box; }
  html, body {
    width: 1200px;
    height: 900px;
    overflow: hidden;
    background: var(--page-bg);
    font-family: "Pathway Gothic One", "Arial Narrow", sans-serif;
  }
  .business-card {
    position: absolute;
    left: 75px;
    top: 150px;
    width: 1050px;
    height: 600px;
    background: var(--card-dark);
    box-shadow: 0 10px 30px rgba(0,0,0,0.18);
    overflow: hidden;
  }
  .brand-band {
    position: absolute;
    inset: 0 0 auto 0;
    height: 270px;
    background: var(--card-light);
  }
  .headphones-art {
    position: absolute;
    top: 40px;
    width: 110px;
    height: 210px;
    background: linear-gradient(180deg, var(--art-grey), #f4f4f4);
    border-radius: 10px;
  }
  .headphones-art.left { left: 36px; }
  .headphones-art.right { right: 36px; top: 20px; height: 190px; }
  .brand-name {
    position: absolute;
    left: 170px;
    top: 8px;
    font-size: 250px;
    line-height: 1;
    color: var(--ink);
    letter-spacing: 4px;
  }
  .info-band {
    position: absolute;
    left: 0;
    right: 0;
    top: 270px;
    bottom: 0;
  }
  .waveform-art {
    position: absolute;
    left: 70px;
    top: 40px;
    width: 640px;
    height: 250px;
    background: radial-gradient(ellipse at 50% 50%, rgba(140,140,140,0.55), rgba(90,90,90,0.25) 55%, transparent 75%);
  }
  .tagline {
    position: absolute;
    left: 40px;
    top: 14px;
    font-size: 30px;
    color: var(--text-light);
  }
  .contact {
    position: absolute;
    display: flex;
    align-items: center;
    gap: 14px;
    color: var(--text-light);
    line-height: 1;
  }
  .contact svg { flex: none; }
  .contact.email { right: 70px; top: 40px; font-size: 48px; }
  .contact.social { right: 70px; top: 115px; font-size: 42px; }
  .contact.phone { left: 40px; top: 150px; font-size: 52px; }
  .contact.web { left: 40px; top: 245px; font-size: 46px; }
</style>
</head>
<body>
  <div class="business-card">
    <div class="brand-band">
      <div class="headphones-art left" role="img" aria-label="Headphones with cord illustration"></div>
      <div class="brand-name">738KV</div>
      <div class="headphones-art right" role="img" aria-label="Headphones with cord illustration"></div>
    </div>

    <div class="info-band">
      <div class="waveform-art" role="img" aria-label="Faint grey audio waveform decoration"></div>
      <p class="tagline">738KV Industry Standard Mixing &amp; Mastering</p>

      <p class="contact email">
        <svg width="52" height="36" viewBox="0 0 52 36" aria-hidden="true">
          <rect x="1.5" y="1.5" width="49" height="33" fill="#f2f2f2" stroke="#2b2a2b" stroke-width="1"/>
          <polyline points="2,2 26,21 50,2" fill="none" stroke="#2b2a2b" stroke-width="2.5"/>
          <polyline points="2,34 20,16 M50,34 32,16" fill="none" stroke="#2b2a2b" stroke-width="2"/>
        </svg>
        <span>sales@738kv.com</span>
      </p>

      <p class="contact social">
        <span>@738KV</span>
      </p>

      <p class="contact phone">
        <svg width="36" height="40" viewBox="0 0 36 40" aria-hidden="true">
          <path d="M8 4 L14 4 L16 13 L11 16 Q14 25 20 30 L24 25 L32 28 L32 34 Q30 38 25 37 Q6 30 4 10 Q4 5 8 4 Z" fill="#f2f2f2"/>
          <path d="M22 6 Q30 8 31 16 M22 12 Q26 13 26 17" fill="none" stroke="#f2f2f2" stroke-width="2"/>
        </svg>
        <span>(555) 214-3907</span>
      </p>

      <p class="contact web">
        <svg width="38" height="38" viewBox="0 0 38 38" aria-hidden="true" fill="none" stroke="#f2f2f2" stroke-width="2.2">
          <circle cx="19" cy="19" r="16"/>
          <ellipse cx="19" cy="19" rx="7" ry="16"/>
          <line x1="3" y1="19" x2="35" y2="19"/>
          <line x1="6" y1="11" x2="32" y2="11"/>
          <line x1="6" y1="27" x2="32" y2="27"/>
        </svg>
        <span>738kv.com</span>
      </p>
    </div>
  </div>
</body>
</html>
```